Postcard Design

I am a practicing Obstetrician and Gynecologist. I am working at a clinic called QRT Verano Care Network. I am looking for a design of a personal advertisement card that can be mailed, handed out, or sent an an electronic copy to the local newspaper to be placed as an ad. I previously worked for another clinic called JLW. They had an ad on my I liked very much, but I cannot use it. It is proprietary to them. I would like something like it. Copy attached. I want my foto and text. I have Printhaven Business Cards with QRT Verano and Stationary already. Access permitted. I would like to stay within that light blue - light green color scheme. I want the card to have me come across as competent and knowledgeable, but also as gentle, compassionate, benevolent, caring, knowledgeable, competent. Obviously, it has to appeal to women.

Target Market(s)

Public, patients, women

Industry/Entity Type

Electronic

Requirements
Nice to have
• A sophisticated, tasteful and inspiring maternity care image is very hard to find. I love the one on my business card. If it or something like it could be found and incorporated, that would be nice. I like a warm, soft, friendly font, Calibri light italic, Archer, Gotham. Describes nicely:Archer, the colorful slab serif. Sweet but not saccharine, earnest but not grave, Archer is designed to hit just the right notes of forthrightness, credibility, and charm.

```html
<!DOCTYPE html>
<html lang="en">
<head>
<meta charset="utf-8">
<title>Dr. Vorhelm – Postcard</title>
<link href="https://fonts.googleapis.com/css2?family=Mulish:wght@300;400;700&family=Zilla+Slab:wght@300&display=swap" rel="stylesheet">
<style>
  :root {
    --page-bg: #ecebe8;
    --panel-blue: #8bbfcf;
    --card-white: #ffffff;
    --text-white: #ffffff;
    --text-soft: #d6e9ef;
    --title-soft: #c4dde5;
    --portrait-tone: #dcdfe6;
    --photo-grey-a: #d9d9d9;
    --photo-grey-b: #8e8e8e;
    --photo-soft-a: #f3ece8;
    --photo-soft-b: #c9b7ae;
    --photo-sepia-a: #e4dccd;
    --photo-sepia-b: #a8987a;
  }
  html, body {
    margin: 0;
    width: 1200px;
    height: 1000px;
    overflow: hidden;
    background: var(--page-bg);
  }
  .postcard {
    position: absolute;
    left: 112px;
    top: 130px;
    width: 955px;
    height: 739px;
    background: var(--card-white);
    box-shadow: 0 2px 10px rgba(0,0,0,.15);
    font-family: "Mulish", sans-serif;
    color: var(--text-white);
  }
  .info-panel {
    position: absolute;
    left: 0; top: 0;
    width: 630px; height: 739px;
    background: var(--panel-blue);
  }
  .portrait {
    position: absolute;
    left: 29px; top: 25px;
    width: 185px; height: 273px;
    background: linear-gradient(180deg, var(--portrait-tone), #f4f4f6);
    box-shadow: 1px 2px 4px rgba(0,0,0,.25);
  }
  .doctor-name {
    position: absolute;
    left: 228px; top: 18px;
    margin: 0;
    font-weight: 700;
    font-size: 24px;
    line-height: 34px;
    white-space: nowrap;
  }
  .doctor-title {
    position: absolute;
    left: 228px; top: 87px;
    margin: 0;
    font-family: "Zilla Slab", serif;
    font-weight: 300;
    font-size: 16.5px;
    letter-spacing: .6px;
    color: var(--title-soft);
    white-space: nowrap;
  }
  .intro {
    position: absolute;
    left: 228px; top: 110px;
    margin: 0;
    font-weight: 300;
    font-size: 21px;
    line-height: 32px;
    white-space: nowrap;
  }
  .intro strong { font-weight: 400; }
  .details {
    position: absolute;
    left: 29px; top: 308px;
    width: 540px;
    font-size: 17px;
    line-height: 26px;
    font-weight: 300;
  }
  .details p { margin: 0; }
  .details .label { font-weight: 400; }
  .contact .phone { font-weight: 400; }
  .plans {
    position: absolute;
    left: 29px; top: 686px;
    margin: 0;
    font-size: 10px;
    line-height: 16px;
    font-weight: 300;
    color: var(--text-soft);
    white-space: nowrap;
  }
  .photo {
    position: absolute;
    left: 638px;
    width: 317px;
  }
  .photo--parent-baby { top: 0; height: 233px; background: linear-gradient(135deg, var(--photo-grey-a), var(--photo-grey-b)); }
  .photo--mother-kiss { top: 243px; height: 265px; background: linear-gradient(120deg, var(--photo-soft-a), var(--photo-soft-b)); }
  .photo--mother-lift { top: 518px; height: 205px; background: linear-gradient(135deg, var(--photo-sepia-b), var(--photo-sepia-a)); }
</style>
</head>
<body>
  <section class="postcard">
    <div class="info-panel">
      <div class="portrait" role="img" aria-label="Portrait photo of Dr. Vorhelm in a white coat"></div>
      <h1 class="doctor-name">Matthias K. (“ Matt ”) Vorhelm,<br>MD, FACOG</h1>
      <p class="doctor-title">Board Certified Obstetrician &amp; Gynecologist</p>
      <p class="intro"><strong>Dr.Vorhelm</strong> is a Board certified OB/GYN<br>and was in private practise in Altanta,<br>Georgia for twenty-five years.<br>He recently was the in-house<br>hospital Obstenics and Gynecology<br>at Harbor Point Memorial Hospital</p>
      <div class="details">
        <p class="label">Education:</p>
        <p>Univeristy of Lindenfeld School of<br>Medicine Germany</p>
        <p class="label">Residency and Internship:</p>
        <p>University of Crestmoor School of Medicine, Kentucky</p>
        <p>Dr. Vorhelm specializes in preventive<br>medicine and womens’s wellness and<br>weight management</p>
        <p class="contact">Accepting New Patients at<br>QRT Verano Care Network<br>214-B Calle Marisol<br>Tamuning, GU 96920<br><span class="phone">671-555-0142</span><br><span class="phone">Fax 671-555-0187</span></p>
      </div>
      <p class="plans">Credentialed Provider with Orvanta Global, Kestrel Shield, Selvano Selectcare,<br>Pelaro Plan, Varnell Plan, QVP, Isolinecare, Brellinwell, Tovarocare, Quillacare. Referral required with some plans.</p>
    </div>
    <div class="photo photo--parent-baby" role="img" aria-label="Black and white photo of a parent holding a baby"></div>
    <div class="photo photo--mother-kiss" role="img" aria-label="Photo of a mother kissing her blue-eyed baby"></div>
    <div class="photo photo--mother-lift" role="img" aria-label="Sepia photo of a mother lifting her baby"></div>
  </section>
</body>
</html>
```